Meadow Crate Co came about when a life change having to do with my health became an issue and I had to change my diet. We’re a homeschool family and learned a more simplistic way to eat and live out our day to day. We’re ready to share how we eat. Included are attachments to give a visual to the concepts in mind. The first attachment is the logo the second is basically the main idea of the company referencing to getting to the roots of nutrition and juicing. The roots design CONCEPT would be incorporated onto the bottle label. The third attachment is representing the clear stickers we’d like to have on bottles. The 4th and Last are the bottle design we’re looking to use. We’d like tall cylinder bottles.

Label must haves :
meadow crate co logo and the quote know your roots
The roots design
MeadowCrateCo.example

```html
<!DOCTYPE html>
<html lang="en">
<head>
<meta charset="utf-8">
<title>Meadow Crate Co — Apple Juice Label</title>
<link rel="stylesheet" href="https://fonts.googleapis.com/css2?family=Jost:wght@700&family=Courier+Prime&family=Arimo:wght@700&display=swap">
<style>
  :root {
    --juice: #f6b01e;
    --juice-deep: #ea9f0f;
    --juice-dark: #d88c0a;
    --ink: #2a2418;
  }
  * { margin: 0; padding: 0; box-sizing: border-box; }
  html, body { width: 900px; height: 1200px; overflow: hidden; background: var(--juice); }
  .label {
    position: relative;
    width: 900px;
    height: 1200px;
    background: var(--juice);
    color: var(--ink);
  }
  .brand {
    position: absolute;
    left: 264px;
    top: 270px;
    width: 200px;
    display: flex;
    align-items: center;
    gap: 12px;
    font-family: "Jost", sans-serif;
    font-weight: 700;
    font-size: 34px;
    line-height: 1.05;
  }
  .brand-dot {
    flex: none;
    width: 16px;
    height: 16px;
    border-radius: 50%;
    background: var(--ink);
  }
  .product {
    position: absolute;
    left: 264px;
    top: 612px;
    width: 205px;
  }
  .product-name {
    font-family: "Jost", sans-serif;
    font-weight: 700;
    font-size: 100px;
    line-height: 0.86;
    letter-spacing: 1px;
    padding-bottom: 14px;
    border-bottom: 2px solid var(--ink);
  }
  .product-type {
    margin-top: 12px;
    font-family: "Courier Prime", monospace;
    font-size: 22px;
    line-height: 1.3;
    letter-spacing: 4px;
    text-transform: uppercase;
  }
  .shake {
    margin-top: 12px;
    display: flex;
    align-items: center;
    gap: 12px;
    border-bottom: 2px solid var(--ink);
    padding-bottom: 6px;
  }
  .shake-badge {
    width: 56px;
    height: 40px;
    border-radius: 5px;
    background: var(--ink);
  }
  .shake-text {
    font-family: "Arimo", sans-serif;
    font-weight: 700;
    font-size: 19px;
    line-height: 1.05;
  }
  .website {
    margin-top: 6px;
    font-family: "Arimo", sans-serif;
    font-weight: 700;
    font-size: 18px;
    white-space: nowrap;
  }
  .volume {
    position: absolute;
    left: 264px;
    top: 1090px;
    width: 205px;
    text-align: right;
    padding-right: 10px;
    font-family: "Courier Prime", monospace;
    font-size: 26px;
  }
  .roots-art {
    position: absolute;
    left: 481px;
    top: 100px;
    width: 160px;
    height: 910px;
    border-radius: 6px;
    background: linear-gradient(180deg, var(--juice-deep), var(--juice-dark));
  }
  .tagline {
    position: absolute;
    left: 580px;
    top: 840px;
    transform: rotate(-90deg);
    transform-origin: left top;
    font-family: "Arimo", sans-serif;
    font-weight: 700;
    font-size: 17px;
    letter-spacing: 3px;
    white-space: nowrap;
  }
</style>
</head>
<body>
  <main class="label">
    <div class="brand">
      <span class="brand-dot"></span>
      <span class="brand-name">Meadow<br>Crate Co</span>
    </div>

    <section class="product">
      <h1 class="product-name">AP<br>PLE</h1>
      <p class="product-type">Fresh<br>Squeezed<br>Juice</p>
      <div class="shake">
        <span class="shake-badge"></span>
        <span class="shake-text">Shake<br>Well</span>
      </div>
      <p class="website">MeadowCrateCo.example</p>
    </section>

    <p class="volume">10 oz</p>

    <div class="roots-art" role="img" aria-label="Line drawing of a young plant: a tall stem with three leaves above and branching roots below"></div>
    <p class="tagline">KNOW YOUR ROOTS</p>
  </main>
</body>
</html>
```